Need web redesign for cybersecurity startup whose mission is to make robust cybersecurity protection

We need a web redesign for Velundra, a cyber security startup. We already have a logo and website but we’re looking for a redesign to reflect the new messaging and positioning of the company – and to update our look with a more polished feel. We’re looking for clean, powerful, confident designs that easily communicate the problems within the cybersecurity space and how Velundra is the answer to those problems.

We can have the long-scrolling stripe layout for the home page, but we don’t want a bunch of interior pages with the same long-scroll format. We’d like to do something a little different and easier to navigate.

Velundra’s products simplify and automate cybersecurity defense so non-experts can successfully protect their information and focus on their business. Velundra’s mission is to provide proactive cybersecurity protection that is easy to use, easy to implement and easy to afford. The designs should reflect this populist message as well as confidence and maybe a little irreverence. Additional key words to describe the company are: secure, protection, easy, everyone.

Velundra offers multiple security products which can both be purchased directly from their site. They provide the world’s most widely used WAF rule set for Wardplex as well as Velundra Guarded Linux (VGL) and Velundra Guarded Linux Kernels to protect Tarnix servers, IoT devices and Podlane containers.

Target Market(s)

IT leaders in small and mid-sized businesses, hosting providers, and enterprise dev ops, product and security groups

Industry/Entity Type

Security

Number of Pages Required

5+ page

Font styles to use
Serif
Sans Serif

Requirements
Must have
• - We can have the long-scrolling stripe layout for the home page, but we don’t want a bunch of interior pages with the same long-scroll format. We’d like to do something a little different and easier to navigate.
• - Clean, powerful, confident designs
• - Real imagery coupled with line designs
Nice to have
• Specific icons to be used for all marketing and web materials for each product:
• - Velund Guarded for Linux (VG/L)
• - WardPlex Rules
• - Velundra Guarded Linux Kernels
• - KRIVE - Commercial Support
• - Guarded OS for Podlane
• - Guarded Apps for Podlane
Should not have
• - No typical imagery for cybersecurity such as binary code, hooded figures, etc.

```html
<!DOCTYPE html>
<html lang="en">
<head>
<meta charset="utf-8">
<title>Velundra — Tarnix Server Protection</title>
<link rel="stylesheet" href="https://fonts.googleapis.com/css2?family=Roboto:wght@400;500;700&family=Open+Sans:wght@400;600;700&display=swap">
<style>
:root{
  --ink:#2f2f2f;
  --text:#3d3d3d;
  --muted:#777;
  --red:#e8464f;
  --orange:#e39a3e;
  --rust:#b0603a;
  --nav:#111;
  --band:#e7e4e0;
  --dark-band:#5b5049;
  --line:#cfcfcf;
  --white:#fff;
  --footer:#f4f2ef;
}
*{box-sizing:border-box;margin:0;padding:0}
html,body{width:1200px;height:4147px;overflow:hidden}
body{font-family:"Open Sans",Arial,sans-serif;color:var(--text);background:var(--white);position:relative}
.section{position:absolute;left:0;width:1200px}
h2.title{font-family:"Roboto",Arial,sans-serif;font-weight:700;font-size:29px;color:var(--ink);text-align:center;text-transform:uppercase;letter-spacing:.3px}
.ornament{position:absolute;left:440px;width:320px;height:14px}
.ornament::before{content:"";position:absolute;left:0;right:0;top:6px;height:1px;background:var(--line)}
.ornament::after{content:"";position:absolute;left:152px;top:0;width:16px;height:14px;border-radius:50%;background:var(--rust);box-shadow:0 0 0 5px var(--white)}
.band .ornament::after{box-shadow:0 0 0 5px var(--band)}

/* header */
.topbar{top:0;height:102px}
.contact-chip{position:absolute;top:30px;display:flex;gap:14px;align-items:flex-start;font-size:16px;line-height:22px;color:var(--ink)}
.brand{position:absolute;left:500px;top:28px;width:200px;display:flex;align-items:center;gap:10px;justify-content:center}
.brand-dot{width:22px;height:22px;border-radius:50%;background:var(--red)}
.brand-name{font-family:"Roboto",Arial,sans-serif;font-weight:700;font-size:22px;color:var(--ink);letter-spacing:1px}
.nav{top:102px;height:45px;background:var(--nav)}
.nav ul{list-style:none;position:absolute;left:102px;top:0;height:45px;display:flex}
.nav li{height:45px;line-height:45px;font-family:"Roboto",sans-serif;font-weight:700;font-size:14px;color:var(--white);text-align:center}
.nav li.active{background:var(--red)}

/* hero */
.hero{top:147px;height:522px;background:linear-gradient(135deg,#9c8f82 0%,#6b5c51 45%,#2a2324 100%)}
.hero-copy{position:absolute;top:330px;width:1200px;text-align:center;font-family:"Roboto",sans-serif;font-weight:700;font-size:29px;line-height:36px;color:var(--white);text-transform:uppercase;text-shadow:0 1px 3px rgba(0,0,0,.5)}

/* intro */
.intro{top:669px;height:349px}
.intro h2{position:absolute;top:48px;width:1200px}
.intro .ornament{top:100px}
.intro p{position:absolute;left:112px;width:976px;top:132px;font-size:14px;line-height:25px;text-align:center}
.tags{position:absolute;top:266px;left:0;width:1200px;display:flex;justify-content:center;gap:22px}
.tag{height:34px;line-height:32px;padding:0 22px;border:1.5px solid #aaa;border-radius:17px;font-size:13px;color:var(--ink)}
.tag.primary{border-color:var(--red);color:var(--red)}

/* partners */
.band{background:var(--band)}
.partners{top:1018px;height:301px}
.partners h2{position:absolute;top:43px;width:1200px}
.partners .ornament{top:96px}
.partner-row{position:absolute;top:146px;left:100px;width:1000px;display:flex;gap:25px}
.partner{width:180px;height:108px;background:var(--white);border:1px solid #d6d3cf;display:flex;align-items:center;justify-content:center}
.partner span{display:block;width:120px;height:36px;border-radius:4px;background:#c9c5c0}

/* video */
.video{top:1319px;height:343px;background:linear-gradient(160deg,#6d6a66 0%,#3a3836 55%,#1e1d1c 100%)}
.video h2{position:absolute;top:100px;width:1200px;color:var(--white);font-family:"Roboto",sans-serif;font-weight:700;font-size:29px;text-align:center}
.play{position:absolute;left:566px;top:158px}

/* quotes */
.quote{text-align:center}
.quote-mark{position:absolute;left:562px;width:76px;height:76px}
.quote-text{position:absolute;width:1200px;font-size:19px;line-height:38px}
.quote-name{position:absolute;width:1200px;font-size:16px}
.quote-role{position:absolute;width:1200px;font-size:13px}
.testimonial{top:1662px;height:329px}
.testimonial .quote-mark{top:47px}
.testimonial .quote-text{top:144px;color:var(--ink)}
.testimonial .quote-name{top:231px;color:var(--red)}
.testimonial .quote-role{top:263px;color:var(--ink)}

/* containers */
.containers{top:1991px;height:276px}
.containers h2{position:absolute;top:44px;width:1200px}
.containers p{position:absolute;left:120px;width:960px;top:130px;font-size:13px;line-height:23px;text-align:center}

/* customers */
.customers{top:2267px;height:423px}
.customers h2{position:absolute;top:40px;width:1200px}
.customers .ornament{top:93px}
.customer-row{position:absolute;top:158px;left:100px;width:1000px;display:flex;gap:42px}
.customer{width:218px;height:218px;border:1px solid #d8d8d8;text-align:center;position:relative}
.customer svg{position:absolute;left:66px;top:28px}
.customer h3{position:absolute;top:165px;width:100%;font-family:"Open Sans",sans-serif;font-weight:600;font-size:14px;color:var(--ink)}

.review{top:2690px;height:296px;background:var(--dark-band)}
.review .quote-mark{top:32px}
.review .quote-text{top:131px;color:var(--white)}
.review .quote-name{top:218px;color:var(--orange)}
.review .quote-role{top:246px;color:var(--white)}

/* blogs */
.blogs{top:2986px;height:514px}
.blogs h2{position:absolute;top:40px;width:1200px}
.blogs .ornament{top:93px}
.post{position:absolute;top:155px;width:470px;height:227px}
.post-frame{position:absolute;left:0;top:0;width:202px;height:227px;border:2px solid var(--orange)}
.post-image{position:absolute;left:10px;top:10px;width:194px;height:217px}
.post-body{position:absolute;left:219px;top:14px;width:260px}
.post-meta{font-size:12px;color:var(--ink);display:flex;gap:16px;align-items:center}
.post-meta span{display:flex;align-items:center;gap:6px}
.post-title{margin-top:20px;font-size:13px;font-weight:600;color:var(--orange)}
.post-text{margin-top:6px;font-size:12.5px;line-height:18.5px;color:var(--ink)}
.read-more{margin-top:10px;font-size:11.5px;font-weight:600;color:var(--ink);display:flex;align-items:center;gap:6px}
.btn{position:absolute;height:34px;line-height:34px;border-radius:17px;background:var(--red);color:var(--white);font-family:"Roboto",sans-serif;font-weight:700;font-size:13px;text-align:center}
.blogs .btn{left:525px;top:428px;width:148px}

/* feeds */
.feeds{top:3500px;height:283px}
.feeds h2{position:absolute;top:44px;width:1200px}
.feeds .ornament{top:94px}
.tweet{position:absolute;top:144px;width:440px;height:94px}
.tweet-avatar{position:absolute;left:0;top:0;width:77px;height:77px}
.tweet-body{position:absolute;left:94px;top:0;width:380px}
.tweet-title{font-size:12.5px;font-weight:700;color:var(--ink)}
.tweet-text{margin-top:3px;font-size:11.5px;line-height:16px;color:var(--ink)}
.tweet-text b{color:#3a7fc1;font-weight:600}
.tweet-meta{margin-top:5px;font-size:11px;color:var(--muted);display:flex;gap:12px;align-items:center}

/* footer */
.footer{top:3783px;height:312px;background:var(--footer);border-top:2px solid #cfc7bd}
.footer h4{position:absolute;top:50px;font-family:"Roboto",sans-serif;font-weight:700;font-size:14px;color:var(--ink);text-transform:uppercase}
.footer h4::after{content:"";position:absolute;left:0;top:26px;width:240px;height:1px;background:#dedad5}
.field{position:absolute;left:100px;width:237px;height:26px;border:1px solid #dcd8d3;background:var(--white);font-size:10px;line-height:24px;padding-left:10px;color:#999}
.footer .btn{left:100px;top:258px;width:86px;height:28px;line-height:28px;font-size:12px}
.detail{position:absolute;left:387px;display:flex;gap:12px;font-size:13px;line-height:19px;color:var(--ink)}
.map{position:absolute;left:686px;top:88px;width:210px;height:174px;background:linear-gradient(135deg,#dfe6d8,#c8d3cf 50%,#e7e1d3)}
.foot-brand{position:absolute;left:912px;top:140px;width:180px;display:flex;align-items:center;justify-content:center;gap:10px}
.bottombar{top:4095px;height:52px;background:var(--orange)}
.bottombar p{position:absolute;left:100px;top:17px;font-size:12px;color:var(--white)}
.social{position:absolute;top:13px;width:26px;height:26px;border-radius:50%;background:#1f5fa8}
</style>
</head>
<body>

<header class="section topbar">
  <div class="contact-chip" style="left:102px">
    <svg width="30" height="30" viewBox="0 0 30 30"><circle cx="15" cy="15" r="13" fill="none" stroke="#e8464f" stroke-width="2"/><path d="M10 8c1-1 2 0 3 2s0 2-1 3c1 2 3 4 5 5 1-1 1-2 3-1s3 2 2 3c-1 2-3 3-6 1-3-2-6-5-7-8s0-4 1-5z" fill="#e8464f"/></svg>
    <div>Call Us:<br>555 014 2280</div>
  </div>
  <div class="brand"><span class="brand-dot"></span><span class="brand-name">VELUNDRA</span></div>
  <div class="contact-chip" style="left:896px">
    <svg width="34" height="28" viewBox="0 0 34 28"><rect x="2" y="3" width="30" height="22" fill="none" stroke="#e8464f" stroke-width="2"/><path d="M2 3l15 12 15-12" fill="none" stroke="#e8464f" stroke-width="2"/></svg>
    <div>Mail Us:<br>info@velundra.com</div>
  </div>
</header>

<nav class="section nav">
  <ul>
    <li class="active" style="width:100px">HOME</li>
    <li style="width:150px">ABOUT US</li>
    <li style="width:170px">WE PROTECT</li>
    <li style="width:145px">SERVICES</li>
    <li style="width:120px">BLOG</li>
    <li style="width:140px">SOCIAL</li>
    <li style="width:170px">CONTACT US</li>
  </ul>
</nav>

<section class="section hero" role="img" aria-label="Video still of a person in an office bracing against a gust, a wall map behind">
  <div class="hero-copy">Don’t be the next cyber victim<br>Harden your shell now</div>
</section>

<section class="section intro">
  <h2 class="title">Tarnix server protection for everyone and everything</h2>
  <div class="ornament"></div>
  <p>Cyber attacks happen. The question is, are you ready? For too many mid-sized and small business the answer is no because they don’t think cyber protection is accessible or made for their needs. Even enterprises often are left unprotected by substandard endpoint protection or none at all. Velundra protects Tarnix servers, web application servers, IoT devices and even Podlane containers. And, it just takes a couple of clicks for complete protection.</p>
  <div class="tags">
    <span class="tag primary">WAF Rules</span>
    <span class="tag">Tarnix Servers</span>
    <span class="tag">IoT Devices</span>
    <span class="tag">Podlane Containers</span>
  </div>
</section>

<section class="section band partners">
  <h2 class="title">More than 20,000 servers protected</h2>
  <div class="ornament"></div>
  <div class="partner-row">
    <div class="partner"><span></span></div>
    <div class="partner"><span></span></div>
    <div class="partner"><span></span></div>
    <div class="partner"><span></span></div>
    <div class="partner"><span></span></div>
  </div>
</section>

<section class="section video" role="img" aria-label="Video still of a tabby cat resting indoors">
  <h2>HARDEN YOUR SHELL NOW</h2>
  <svg class="play" width="68" height="68" viewBox="0 0 68 68"><circle cx="34" cy="34" r="31" fill="none" stroke="#fff" stroke-width="3"/><path d="M27 21l22 13-22 13z" fill="#fff"/></svg>
</section>

<section class="section testimonial quote">
  <svg class="quote-mark" viewBox="0 0 76 76"><circle cx="38" cy="38" r="36" fill="none" stroke="#e8464f" stroke-width="2"/><path d="M24 44v-7c0-6 3-10 9-12l1 3c-3 1-5 4-5 6h5v10zM41 44v-7c0-6 3-10 9-12l1 3c-3 1-5 4-5 6h5v10z" fill="none" stroke="#e8464f" stroke-width="2"/></svg>
  <p class="quote-text">We trust our server security to Velundra Guarded Tarnix because it works. We’ve used it for years<br>and it has been essential in keeping dark forces at bay.</p>
  <p class="quote-name">Rowan Teller</p>
  <p class="quote-role">Brightmoss Studio</p>
</section>

<section class="section band containers">
  <h2 class="title">Yes. You can secure Podlane containers</h2>
  <p>Podlane is the fastest growing application developer software in the world. But, people don’t realize that their containers are wide open to cyber attacks. Velundra provides a secure OS kernel that is inherited by all containers on a single server. It’s easy to install, doesn’t impact performance and protects your containers against malicious attacks immediately.</p>
</section>

<section class="section customers">
  <h2 class="title">Type of customers we serve</h2>
  <div class="ornament"></div>
  <div class="customer-row">
    <div class="customer">
      <svg width="86" height="90" viewBox="0 0 86 90"><g fill="#bfe3ef" stroke="#2d6f96" stroke-width="2"><rect x="10" y="4" width="66" height="18" rx="2"/><rect x="10" y="26" width="66" height="18" rx="2"/><rect x="10" y="48" width="66" height="18" rx="2"/></g><g fill="#2d6f96"><circle cx="20" cy="13" r="2.5"/><circle cx="20" cy="35" r="2.5"/><circle cx="20" cy="57" r="2.5"/></g><path d="M43 66v12M8 80h70" stroke="#2d6f96" stroke-width="2"/><circle cx="43" cy="80" r="5" fill="#fff" stroke="#2d6f96" stroke-width="2"/></svg>
      <h3>Hosting Providers</h3>
    </div>
    <div class="customer">
      <svg width="86" height="90" viewBox="0 0 86 90"><g fill="#bfe3ef" stroke="#2d6f96" stroke-width="2"><rect x="14" y="20" width="24" height="64"/><rect x="38" y="6" width="30" height="78"/></g><g stroke="#2d6f96" stroke-width="2"><path d="M20 30h12M20 40h12M20 50h12M20 60h12M20 70h12M45 16v58M53 16v58M61 16v58"/><path d="M6 84h74"/></g></svg>
      <h3>Enterprises</h3>
    </div>
    <div class="customer">
      <svg width="86" height="90" viewBox="0 0 86 90"><rect x="6" y="8" width="74" height="54" rx="2" fill="#bfe3ef" stroke="#2d6f96" stroke-width="2"/><rect x="12" y="14" width="62" height="42" fill="#fff" stroke="#2d6f96" stroke-width="1.5"/><path d="M16 48l12-12 10 8 14-16 18 10" fill="none" stroke="#2d6f96" stroke-width="2"/><path d="M36 62l-4 14h22l-4-14M26 78h34" fill="none" stroke="#2d6f96" stroke-width="2"/></svg>
      <h3>Mid-sized &amp; Small Business</h3>
    </div>
    <div class="customer">
      <svg width="86" height="90" viewBox="0 0 86 90"><rect x="6" y="6" width="74" height="56" rx="3" fill="#2b2b2b"/><rect x="12" y="12" width="62" height="42" fill="#9ad8cf"/><rect x="34" y="24" width="18" height="18" fill="#fff"/><path d="M38 33l3 3 7-7" fill="none" stroke="#2b2b2b" stroke-width="2"/><path d="M34 62l-3 14h24l-3-14M24 78h38" fill="none" stroke="#2b2b2b" stroke-width="2.5"/></svg>
      <h3>IoT OEMs</h3>
    </div>
  </div>
</section>

<section class="section review quote">
  <svg class="quote-mark" viewBox="0 0 76 76"><circle cx="38" cy="38" r="36" fill="none" stroke="#e39a3e" stroke-width="2"/><path d="M24 44v-7c0-6 3-10 9-12l1 3c-3 1-5 4-5 6h5v10zM41 44v-7c0-6 3-10 9-12l1 3c-3 1-5 4-5 6h5v10z" fill="none" stroke="#e39a3e" stroke-width="2"/></svg>
  <p class="quote-text">Velundra eliminated 80% of our shared server issues overnight. And, it saves us about four<br>hours of staff time every day because it protects servers automatically.</p>
  <p class="quote-name">Rowan Teller</p>
  <p class="quote-role">Brightmoss Studio</p>
</section>

<section class="section blogs">
  <h2 class="title">Latest blogs</h2>
  <div class="ornament"></div>
  <article class="post" style="left:100px">
    <div class="post-frame"></div>
    <div class="post-image" role="img" aria-label="Photo of a keyboard with a red padlock key" style="background:linear-gradient(135deg,#4e9fd6,#1f5f9e 60%,#c9303a)"></div>
    <div class="post-body">
      <div class="post-meta"><span>▦ 08 May</span><span>● Admin</span></div>
      <p class="post-title">Lorem ipsum dolor sit laoreet l amet...</p>
      <p class="post-text">Lorem ipsum dolor sit aconsectetuer adip iscing elit, sediam nonummy nibh euismod tincidunt ut laoreet dolore magna aliquam erat volutpat. Ut wisi enim adedianonummy nibh.</p>
      <p class="read-more">Read More <svg width="14" height="14" viewBox="0 0 14 14"><circle cx="7" cy="7" r="6" fill="none" stroke="#2f2f2f"/><path d="M5 4l3 3-3 3" fill="none" stroke="#2f2f2f"/></svg></p>
    </div>
  </article>
  <article class="post" style="left:620px">
    <div class="post-frame"></div>
    <div class="post-image" role="img" aria-label="Photo of a person working at a laptop" style="background:linear-gradient(135deg,#dfe8ee,#9fb6c6 50%,#4f5f6e)"></div>
    <div class="post-body">
      <div class="post-meta"><span>▦ 08 May</span><span>● Admin</span></div>
      <p class="post-title">Lorem ipsum dolor sit laoreet l amet...</p>
      <p class="post-text">Lorem ipsum dolor sit aconsectetuer adip iscing elit, sediam nonummy nibh euismod tincidunt ut laoreet dolore magna aliquam erat volutpat. Ut wisi enim adedianonummy nibh.</p>
      <p class="read-more">Read More <svg width="14" height="14" viewBox="0 0 14 14"><circle cx="7" cy="7" r="6" fill="none" stroke="#2f2f2f"/><path d="M5 4l3 3-3 3" fill="none" stroke="#2f2f2f"/></svg></p>
    </div>
  </article>
  <div class="btn">VIEW ALL BLOG</div>
</section>

<section class="section band feeds">
  <h2 class="title">Social feeds</h2>
  <div class="ornament"></div>
  <div class="tweet" style="left:100px">
    <div class="tweet-avatar" role="img" aria-label="Author photo" style="background:linear-gradient(135deg,#c9b9a8,#6d5a4c)"></div>
    <div class="tweet-body">
      <p class="tweet-title">Lorem ipsum dolor sit onsectetue lorem ipsum sit dolor</p>
      <p class="tweet-text"><b>@velundrahq</b> Lorem ipsum dolor sit amet, consectetuers, jgadips elit, sed diam sit nonummy nibhjty vmo euismod tincidunt vulputae magna aliquam erat laoreet dolore...</p>
      <p class="tweet-meta"><span>♡ ⇪</span><span>◷ 24 Hours ago</span></p>
    </div>
  </div>
  <div class="tweet" style="left:636px">
    <div class="tweet-avatar" role="img" aria-label="Author photo" style="background:linear-gradient(135deg,#b8b2ab,#5a534d)"></div>
    <div class="tweet-body">
      <p class="tweet-title">Lorem ipsum dolor sit onsectetue lorem ipsum sit dolor</p>
      <p class="tweet-text"><b>@velundrahq</b> Lorem ipsum dolor sit amet, consectetuers, jgadips elit, sed diam sit nonummy nibhjty vmo euismod tincidunt vulputae magna aliquam erat laoreet dolore...</p>
      <p class="tweet-meta"><span>♡ ⇪</span><span>◷ 24 Hours ago</span></p>
    </div>
  </div>
</section>

<footer class="section footer">
  <h4 style="left:100px">Quick Inquiry</h4>
  <div class="field" style="top:102px">Your Name</div>
  <div class="field" style="top:143px">Phone</div>
  <div class="field" style="top:184px">Email</div>
  <div class="field" style="top:223px">Message</div>
  <div class="btn">SUBMIT</div>

  <h4 style="left:387px">Contact Details</h4>
  <div class="detail" style="top:98px">
    <svg width="14" height="20" viewBox="0 0 14 20"><path d="M7 1a6 6 0 0 1 6 6c0 5-6 12-6 12S1 12 1 7a6 6 0 0 1 6-6z" fill="#e39a3e"/><circle cx="7" cy="7" r="2.3" fill="#fff"/></svg>
    <div><b>VELUNDRA</b><br>48 Quarry Lane, Ashford Road,<br>Opp Ridge Street, CA - 904411</div>
  </div>
  <div class="detail" style="top:184px">
    <svg width="14" height="16" viewBox="0 0 14 16"><path d="M3 1c1-1 2 0 3 2s0 2-1 3c1 2 2 3 4 4 1-1 1-2 3-1s2 2 1 3c-1 2-3 3-6 1S1 8 1 5s1-3 2-4z" fill="#e39a3e"/></svg>
    <div>555 014 2280</div>
  </div>
  <div class="detail" style="top:220px">
    <svg width="16" height="14" viewBox="0 0 16 14"><rect x="1" y="2" width="14" height="10" fill="#e39a3e"/><path d="M1 2l7 6 7-6" fill="none" stroke="#fff" stroke-width="1.2"/></svg>
    <div>info@velundra.com</div>
  </div>

  <h4 style="left:686px">Location Map</h4>
  <div class="map" role="img" aria-label="Street map showing the office location"></div>
  <div class="foot-brand"><span class="brand-dot"></span><span class="brand-name">VELUNDRA</span></div>
</footer>

<div class="section bottombar">
  <p>Copyright © 2017 VELUNDRA ®. All Rights Reserved.</p>
  <span class="social" style="left:991px"></span>
  <span class="social" style="left:1032px"></span>
  <span class="social" style="left:1071px"></span>
</div>

</body>
</html>
```